The Timber Quill Album Cover and Logo Update

We are a covers band called 'The Timber Quill' based in Austria. We are releasing an originals CD (English written songs) in December of this year and need artwork for our CD (6 page DigiPak with possible diecut). The album will be called 'Harbour Lanterns' and will consist of 13 songs in an acoustic/pop rock style with small hints of country influences. Our website has a sleek feel with our main colours being dark grey, black, white, with hints of lime green. These are colours that we would like to incorporate into the album artwork. We are open to different interpretations of a 'modern acoustic feel' and would like to filter this down to our website and hopefully some band merchandise, therefore we would require files in different formats that would be suitable to send to print companies or to uploads onto websites, etc. Taking inspiration from acoustic type cladding that would normally be found inside a recording studio (see attachments) which we feel would make it a simple but effective cover.
So we would need:
- The main front cover
- The back page with the songs listed (published by...)
- Inside front cover (left panel) *1
- Inside middle (where the CD)
- The CD itself- Inside right cover *2
- Outside back page *3
* the inside/back page (*1 *2 *3) artwork will be as a background as there will be some text and photos here.
Our logo is a black and white acoustic guitar outline with the band name written inside: we would like this to be updated to fit the sleek look of the band and incorporate a bit of the lime green within in it and add 'and more' into the band name. We would like to keep the font and the text with the additional text added in (THE TIMBER QUILL and more - Lounge-Bar-Party) . www.thetimberquill-demo.com

Logo Text

THE TIMBER QUILL 'and more' (lounge - bar - party)

Colors
9bcb3c

Requirements
Must have
• A hint of limegreen on the front cover.
• The album name.
Should not have
• No band pictures or guitars on the front or back cover, I would like something unique, something special, that makes it stand out, maybe something drawn by hand, or elements with colour splashes (Lime Green), or maybe even just the logo (redesigned).
• And the inside should be more of a background image, with the pictures added to it.
• A continuous theme throughout.

```html
<!DOCTYPE html>
<html lang="en">
<head>
<meta charset="utf-8">
<title>The Timber Quill – Harbour Lanterns CD artwork</title>
<link rel="stylesheet" href="https://fonts.googleapis.com/css2?family=Open+Sans:wght@400;600&family=Orbitron:wght@600&display=swap">
<style>
  :root {
    --stage: #e9e9e9;
    --ink-black: #07090a;
    --deep-green: #16241a;
    --moss: #2f4a32;
    --lime: #9bcb3c;
    --pale: #e4f0d8;
    --muted: #9fb39a;
  }
  * { box-sizing: border-box; margin: 0; padding: 0; }
  html, body { width: 1200px; height: 720px; overflow: hidden; }
  body {
    background: var(--stage);
    font-family: "Open Sans", sans-serif;
    position: relative;
  }
  .texture {
    position: absolute; inset: 0;
    background:
      radial-gradient(ellipse at 62% 62%, rgba(120,170,110,.35) 0%, rgba(47,74,50,.25) 30%, transparent 65%),
      linear-gradient(160deg, var(--ink-black) 0%, var(--deep-green) 55%, #0c130e 100%);
  }
  /* open digipak spread */
  .digipak {
    position: absolute; left: 40px; top: 30px;
    width: 760px; height: 380px;
    display: flex;
    box-shadow: 0 6px 18px rgba(0,0,0,.25);
  }
  .panel { position: relative; width: 380px; height: 380px; overflow: hidden; }
  .panel-back .spine {
    position: absolute; right: 0; top: 0; width: 16px; height: 100%;
    background: var(--lime);
  }
  .tracklist-block {
    position: absolute; left: 34px; top: 112px; color: var(--pale);
  }
  .published {
    font-family: "Orbitron", sans-serif; font-weight: 600;
    font-size: 11px; letter-spacing: 1.5px; text-transform: uppercase;
    margin-bottom: 12px;
  }
  .tracks { list-style: none; font-size: 13px; line-height: 1.32; }
  /* band name lockup */
  .lockup { position: absolute; color: var(--pale); white-space: nowrap; }
  .wordmark {
    display: flex; align-items: center; gap: 10px; font-weight: 600;
  }
  .wordmark .dot {
    width: 12px; height: 12px; border-radius: 50%; background: var(--lime);
  }
  .tagline {
    display: flex; gap: 14px; align-items: baseline;
    margin-left: 22px; margin-top: 2px;
    font-size: 11px; letter-spacing: 1px;
  }
  .tagline .and-more { color: var(--lime); font-weight: 600; text-transform: none; letter-spacing: 0; }
  .tagline .genres { text-transform: uppercase; }
  .album-title {
    margin-left: 22px; margin-top: 10px;
    font-family: "Orbitron", sans-serif; font-weight: 600;
    font-size: 11px; letter-spacing: 1.5px; text-transform: uppercase; color: var(--muted);
  }
  .panel-front .lockup { left: 60px; top: 140px; }
  .panel-front .wordmark { font-size: 28px; }
  .made-in { position: absolute; color: var(--muted); font-size: 10px; }
  /* booklet */
  .booklet {
    position: absolute; left: 840px; top: 330px; width: 320px; height: 320px;
    overflow: hidden; box-shadow: 0 6px 18px rgba(0,0,0,.25);
  }
  .booklet .lockup { left: 36px; top: 124px; }
  .booklet .wordmark { font-size: 26px; }
  .booklet .made-in { right: 22px; bottom: 22px; }
  /* disc */
  .disc {
    position: absolute; left: 340px; top: 428px; width: 280px; height: 280px;
    border-radius: 50%; overflow: hidden;
    border: 5px solid #f4f4f4;
    box-shadow: 0 6px 18px rgba(0,0,0,.3);
  }
  .disc .lockup { left: 46px; top: 48px; }
  .disc .wordmark { font-size: 19px; gap: 8px; }
  .disc .wordmark .dot { width: 9px; height: 9px; }
  .disc .tagline { font-size: 9px; margin-left: 17px; gap: 10px; }
  .disc .made-in { left: 132px; bottom: 38px; }
  .disc .hole {
    position: absolute; left: 50%; top: 50%; width: 50px; height: 50px;
    margin: -25px 0 0 -25px; border-radius: 50%;
    background: var(--stage); border: 7px solid #d8d8d8;
  }
</style>
</head>
<body>
  <section class="digipak">
    <div class="panel panel-back">
      <div class="texture" role="img" aria-label="Dark green grunge texture of studio acoustic cladding"></div>
      <div class="spine"></div>
      <div class="tracklist-block">
        <p class="published">Harbour Lanterns published by …</p>
        <ol class="tracks">
          <li>1. Days of Gold</li>
          <li>2. Devil at your Heels</li>
          <li>3. Guilty soul of Mine</li>
          <li>4. How could I?</li>
          <li>5. Live your Life</li>
          <li>6. Lost, Down &amp; Gone</li>
          <li>7. Sad Eyes</li>
          <li>8. Show Me</li>
          <li>9. The Fall</li>
          <li>10. The Road</li>
          <li>11. This heart of Yours</li>
          <li>12. What a Show</li>
          <li>13. World to Come</li>
        </ol>
      </div>
    </div>
    <div class="panel panel-front">
      <div class="texture" role="img" aria-label="Dark green grunge texture of studio acoustic cladding with light streaks"></div>
      <div class="lockup">
        <div class="wordmark"><span class="dot"></span>The Timber Quill</div>
        <div class="tagline"><span class="genres">Lounge-Bar-Party</span><span class="and-more">and more</span></div>
        <p class="album-title">Harbour Lanterns</p>
      </div>
    </div>
  </section>

  <div class="disc">
    <div class="texture" role="img" aria-label="Dark green grunge texture of studio acoustic cladding"></div>
    <div class="lockup">
      <div class="wordmark"><span class="dot"></span>The Timber Quill</div>
      <div class="tagline"><span class="genres">Lounge-Bar-Party</span><span class="and-more">and more</span></div>
    </div>
    <p class="made-in">Made in Austria</p>
    <div class="hole"></div>
  </div>

  <section class="booklet">
    <div class="texture" role="img" aria-label="Dark green grunge texture of studio acoustic cladding with light streak"></div>
    <div class="lockup">
      <div class="wordmark"><span class="dot"></span>The Timber Quill</div>
      <div class="tagline"><span class="genres">Lounge-Bar-Party</span><span class="and-more">and more</span></div>
    </div>
    <p class="made-in">Made in Austria</p>
  </section>
</body>
</html>
```